Recherche d'une étiquette pour une bouteille de vin

I need a wine label for a Spanish Almena del Cierzo wine.
The wine already exist burt the label is quiete ugly (see attached)
I've made a firsrt research but I don't like it (pdf attached)

Je cherche a faire une étiquette pur du vin de la Almena del Cierzo.
Le vin existe déjà mais l'étiquette est très moche.
J'ai fais une 1ere recherche mais elle ne me plaît pas (pdf joint)

Target Market(s)

Suisse espagne

Industry/Entity Type

Vineyard

Colors

Designer to choose colors to be used in the design.

Requirements
Must have
• Please use black color + 2 pantone color
• Merci d'utiliser le noir + 2 couleur pantone
• Format: 54 x 124mm
Nice to have
• Le logo Almena del Cierzo (joint)

```html
<!DOCTYPE html>
<html lang="es">
<head>
<meta charset="utf-8">
<title>Velden Aurum 2017 — Almena del Cierzo label series</title>
<link rel="stylesheet" href="https://fonts.googleapis.com/css2?family=Bodoni+Moda:wght@400;500&family=Cormorant+Garamond:wght@500;600&family=Josefin+Sans:wght@400&display=swap">
<style>
  :root {
    --backdrop: #3f3f41;
    --paper: #fbfbfa;
    --wine: #8e1b24;
    --ink: #1c1c1c;
    --gold: #b99a5b;
    --silver-dark: #b9bbbd;
    --silver-light: #f2f2f2;
    --hairline: #c9c9c9;
  }
  * { box-sizing: border-box; margin: 0; padding: 0; }
  html, body { width: 1200px; height: 900px; overflow: hidden; }
  body {
    background: var(--backdrop);
    position: relative;
    font-family: "Cormorant Garamond", Georgia, serif;
    color: var(--ink);
  }

  .label {
    position: absolute;
    top: 200px;
    width: 230px;
    height: 470px;
    background: var(--paper);
    overflow: hidden;
    box-shadow: 0 6px 18px rgba(0,0,0,.35);
  }
  .label--silver { left: 60px;
    background: linear-gradient(90deg, var(--silver-dark) 0, var(--silver-light) 7%, var(--paper) 14%, var(--paper) 86%, var(--silver-light) 93%, var(--silver-dark) 100%); }
  .label--framed { left: 345px; }
  .label--ruled { left: 630px; }
  .label--arched { left: 915px; border-radius: 115px 115px 10px 10px; }

  /* brand name */
  .brand {
    position: absolute;
    font-family: "Bodoni Moda", Georgia, serif;
    font-weight: 400;
    color: var(--ink);
    line-height: 1;
    letter-spacing: .02em;
  }
  .label--silver .brand {
    left: 14px; top: 420px;
    transform-origin: left top;
    transform: rotate(-90deg);
    font-size: 30px; white-space: nowrap;
  }
  .label--framed .brand,
  .label--ruled .brand { left: 26px; top: 36px; font-size: 28px; width: 190px; }
  .vintage {
    position: absolute;
    font-family: "Bodoni Moda", Georgia, serif;
    font-size: 14px; color: var(--ink);
  }
  .label--silver .vintage { left: 40px; top: 48px; transform: rotate(-90deg); }
  .label--framed .vintage,
  .label--ruled .vintage { left: 152px; top: 100px; }

  .seal {
    position: absolute; left: 55px; top: 18px;
    width: 120px; height: 120px; border-radius: 50%;
    background: var(--wine);
    display: flex; flex-direction: column; align-items: center; justify-content: center;
  }
  .seal .brand { position: static; color: var(--paper); font-size: 20px; text-align: center; }
  .seal .vintage { position: static; color: var(--paper); margin-top: 6px; }

  /* appellation name: plain words, one size, one weight, one colour */
  .appellation {
    position: absolute;
    font-family: "Bodoni Moda", Georgia, serif;
    font-weight: 400;
    font-size: 38px;
    line-height: 1.12;
    color: var(--wine);
    white-space: nowrap;
  }
  .label--silver .appellation { left: 78px; top: 110px; }
  .label--framed .appellation,
  .label--ruled .appellation { left: 60px; top: 160px; }
  .label--arched .appellation { left: 60px; top: 175px; }

  .council {
    position: absolute;
    font-family: "Josefin Sans", Arial, sans-serif;
    font-size: 6.5px; letter-spacing: .04em; text-transform: uppercase;
    color: var(--wine);
    transform-origin: left top; transform: rotate(-90deg);
    white-space: nowrap;
  }
  .label--silver .council { left: 64px; top: 300px; }
  .label--framed .council,
  .label--ruled .council { left: 46px; top: 340px; }
  .label--arched .council { left: 48px; top: 350px; }

  .producer {
    position: absolute;
    font-size: 7.5px; line-height: 1.35; text-transform: uppercase;
    color: var(--ink); letter-spacing: .03em;
  }
  .label--silver .producer { left: 80px; top: 330px; }
  .label--framed .producer,
  .label--ruled .producer { left: 60px; top: 360px; }
  .label--arched .producer { left: 60px; top: 368px; }

  .origin {
    position: absolute;
    font-size: 7.5px; text-transform: uppercase; letter-spacing: .05em;
    color: var(--wine);
    border-bottom: 1px solid var(--wine);
    padding-bottom: 2px; width: 120px;
  }
  .label--silver .origin { left: 80px; top: 385px; }
  .label--framed .origin,
  .label--ruled .origin { left: 110px; top: 412px; width: 100px; }
  .label--arched .origin { left: 60px; top: 420px; }

  .specs {
    position: absolute; display: flex; justify-content: space-between;
    font-size: 7.5px; text-transform: uppercase; letter-spacing: .04em;
    color: var(--ink);
  }
  .label--silver .specs { left: 80px; top: 404px; width: 130px; }
  .label--framed .specs,
  .label--ruled .specs { left: 26px; top: 436px; width: 180px; }
  .label--arched .specs { left: 60px; top: 438px; width: 140px; }

  .band {
    position: absolute; left: 0; right: 0; top: 424px; height: 20px;
    background: var(--wine);
  }
  .frame {
    position: absolute; inset: 12px;
    border: 1px solid var(--gold);
  }
  .rule {
    position: absolute; top: 14px; bottom: 14px; width: 1px;
    background: var(--hairline);
  }
  .rule--left { left: 16px; }
  .rule--right { right: 16px; }
</style>
</head>
<body>

<section class="label label--silver" aria-label="Etiqueta variante plateada">
  <p class="brand">Velden Aurum</p>
  <p class="vintage">2017</p>
  <p class="appellation">Almena<br>del<br>Cierzo</p>
  <p class="council">Consejo regulador de la denominación de origen</p>
  <p class="producer">Elaborado por bodegas<br>Velden Aurum S.L.<br>en Camino Alto<br>Villarreal del Campo<br>Soria — España</p>
  <p class="origin">Product of Spain</p>
  <div class="specs"><span>Alc. 14% by vol.</span><span>750ml</span></div>
  <div class="band"></div>
</section>

<section class="label label--framed" aria-label="Etiqueta variante con marco dorado">
  <div class="frame"></div>
  <p class="brand">VELDEN AURUM</p>
  <p class="vintage">2017</p>
  <p class="appellation">Almena<br>del<br>Cierzo</p>
  <p class="council">Consejo regulador de la denominación de origen</p>
  <p class="producer">Elaborado por bodegas<br>Velden Aurum S.L.<br>en Camino Alto<br>Villarreal del Campo<br>Soria — España</p>
  <p class="origin">Product of Spain</p>
  <div class="specs"><span>Alc. 14% by vol.</span><span>750ml</span></div>
</section>

<section class="label label--ruled" aria-label="Etiqueta variante con filetes laterales">
  <div class="rule rule--left"></div>
  <div class="rule rule--right"></div>
  <p class="brand">VELDEN AURUM</p>
  <p class="vintage">2017</p>
  <p class="appellation">Almena<br>del<br>Cierzo</p>
  <p class="council">Consejo regulador de la denominación de origen</p>
  <p class="producer">Elaborado por bodegas<br>Velden Aurum S.L.<br>en Camino Alto<br>Villarreal del Campo<br>Soria — España</p>
  <p class="origin">Product of Spain</p>
  <div class="specs"><span>Alc. 14% by vol.</span><span>750ml</span></div>
</section>

<section class="label label--arched" aria-label="Etiqueta variante en arco con sello">
  <div class="seal">
    <p class="brand">Velden<br>Aurum</p>
    <p class="vintage">2017</p>
  </div>
  <p class="appellation">Almena<br>del<br>Cierzo</p>
  <p class="council">Consejo regulador de la denominación de origen</p>
  <p class="producer">Elaborado por bodegas<br>Velden Aurum S.L.<br>en Camino Alto<br>Villarreal del Campo<br>Soria — España</p>
  <p class="origin">Product of Spain</p>
  <div class="specs"><span>Alc. 14% by vol.</span><span>750ml</span></div>
</section>

</body>
</html>
```